Business card design needed

We need a buisness card design to suit our buisness "Maple Parcel", a company on the south coast of Australia, a wholesale greeting card and gift wrap buisness. We are open to different colour options possibly some pastels. A card that got my attention was'the ''hoofnotes.com.au'' buisness card. I liked the colour scheme, layout, and the use of a cartoon image, but am also open to all ideas.

Industry/Entity Type

Business

Contact Information for Business Card

Maple Parcel Unit 37 / 18 Banksia ave West Torrin 2563 ph 0244879351 fax 0244879352 Colin Madsey email maple.parcel@postvale.com

```html
<!DOCTYPE html>
<html lang="en">
<head>
<meta charset="utf-8">
<title>Maple Parcel – Business Card</title>
<link rel="stylesheet" href="https://fonts.googleapis.com/css2?family=Ubuntu:wght@500;700&family=Roboto+Slab:wght@500&display=swap">
<style>
  :root {
    --canvas: #ffffff;
    --card-light-1: #ffffff;
    --card-light-2: #d9d9d9;
    --card-dark-1: #3a3a3a;
    --card-dark-2: #0c0c0c;
    --ink-dark: #1a1a1a;
    --ink-grey: #555555;
    --ink-light: #ffffff;
    --name-light: #dcdcdc;
    --tag-grey: #777777;
    --red: #e31b23;
    --red-deep: #9e1218;
  }
  * { box-sizing: border-box; margin: 0; padding: 0; }
  html, body { width: 1200px; height: 1000px; overflow: hidden; background: var(--canvas); }
  .canvas { position: relative; width: 1200px; height: 1000px; }

  .card {
    position: absolute;
    width: 562px; height: 323px;
    border-radius: 0 36px 0 36px;
    overflow: hidden;
    box-shadow: 0 3px 8px rgba(0,0,0,0.25);
    font-family: "Ubuntu", sans-serif;
  }
  .card--light { left: 90px; top: 137px; background: radial-gradient(ellipse at 35% 30%, var(--card-light-1) 0%, var(--card-light-2) 100%); }
  .card--dark  { left: 557px; top: 548px; background: radial-gradient(ellipse at 55% 55%, var(--card-dark-1) 0%, var(--card-dark-2) 100%); }

  .card__art { position: absolute; inset: 0; width: 562px; height: 323px; }

  .brand { position: absolute; left: 27px; top: 22px; text-align: right; }
  .brand__name { font-weight: 700; font-size: 21px; line-height: 1; letter-spacing: -0.2px; }
  .brand__tag { font-family: "Roboto Slab", serif; font-weight: 500; font-size: 8.5px; margin-top: 1px; }
  .card--light .brand__name { color: var(--ink-dark); }
  .card--light .brand__tag { color: var(--tag-grey); }
  .card--dark .brand__name { color: var(--ink-light); }
  .card--dark .brand__tag { color: #bbbbbb; }

  .holder {
    position: absolute; right: 48px; top: 104px;
    font-weight: 500; font-size: 32px; line-height: 1;
  }
  .card--light .holder { color: var(--ink-dark); }
  .card--dark .holder { color: var(--name-light); }

  .contacts { position: absolute; right: 44px; top: 148px; list-style: none; }
  .contacts li {
    display: flex; justify-content: flex-end; align-items: center;
    height: 23.5px; font-weight: 700; font-size: 13px;
  }
  .card--light .contacts li { color: var(--ink-grey); }
  .card--dark .contacts li { color: var(--ink-light); }
  .contacts svg { width: 20px; height: 18px; margin-left: 10px; }
  .card--light .contacts svg { fill: var(--ink-grey); stroke: var(--ink-grey); }
  .card--dark .contacts svg { fill: var(--ink-light); stroke: var(--ink-light); }
</style>
</head>
<body>
<div class="canvas">

  <!-- Light card -->
  <section class="card card--light">
    <svg class="card__art" viewBox="0 0 562 323" aria-hidden="false">
      <defs>
        <linearGradient id="redBandA" x1="0" x2="1">
          <stop offset="0" stop-color="#9e1218"/><stop offset="0.4" stop-color="#e31b23"/><stop offset="1" stop-color="#b3141b"/>
        </linearGradient>
        <linearGradient id="baseDark" x1="0" y1="0" x2="0" y2="1">
          <stop offset="0" stop-color="#2a2a2a"/><stop offset="1" stop-color="#0c0c0c"/>
        </linearGradient>
        <linearGradient id="bowTone" x1="0" y1="0" x2="1" y2="1">
          <stop offset="0" stop-color="#e52a2f"/><stop offset="1" stop-color="#a8141a"/>
        </linearGradient>
      </defs>
      <path fill="#111" d="M0,214 C120,200 260,256 400,268 C470,274 530,254 562,232 L562,323 L0,323 Z"/>
      <path fill="url(#redBandA)" d="M0,218 C120,205 260,260 400,272 C470,278 530,258 562,238 L562,248 C500,272 440,280 380,278 C260,272 130,232 0,244 Z"/>
      <path fill="url(#redBandA)" d="M0,250 C130,240 260,280 380,286 C450,289 520,272 562,256 L562,260 C460,292 350,302 250,288 C150,274 60,282 0,296 Z"/>
      <path fill="url(#baseDark)" d="M0,300 C80,286 170,282 260,293 C360,305 470,290 562,262 L562,323 L0,323 Z"/>
      <path fill="url(#bowTone)" role="img" aria-label="Red gift ribbon bow tied across the corner" d="M467,0 L562,0 L562,86 C540,80 520,70 505,50 C490,32 475,16 467,0 Z"/>
    </svg>
    <div class="brand">
      <div class="brand__name">Maple Parcel</div>
      <div class="brand__tag">greeting card and gift wrap</div>
    </div>
    <div class="holder">Colin Madsey</div>
    <ul class="contacts">
      <li>Unit 37 / 18 Banksia ave West Torrin 2563
        <svg viewBox="0 0 20 18"><path stroke="none" d="M10,1 L19,9 L16.5,9 L16.5,17 L12,17 L12,12 L8,12 L8,17 L3.5,17 L3.5,9 L1,9 Z"/></svg></li>
      <li>0244879351
        <svg viewBox="0 0 20 18"><path stroke="none" d="M2,6 C2,2 18,2 18,6 L15,7 L14,5 C12,4 8,4 6,5 L5,7 Z M5,9 L15,9 L18,16 L2,16 Z"/></svg></li>
      <li>0244879352
        <svg viewBox="0 0 20 18"><path stroke="none" d="M5,1 L15,1 L15,7 L5,7 Z M1,8 L19,8 L19,17 L1,17 Z"/><path stroke="none" fill="#ddd" d="M4,11 L16,11 L16,12.5 L4,12.5 Z"/></svg></li>
      <li>maple.parcel@postvale.com
        <svg viewBox="0 0 20 18"><text x="10" y="15" text-anchor="middle" font-size="18" font-family="Ubuntu, sans-serif" stroke="none">@</text></svg></li>
    </ul>
  </section>

  <!-- Dark card -->
  <section class="card card--dark">
    <svg class="card__art" viewBox="0 0 562 323">
      <path fill="#050505" d="M0,214 C120,200 260,256 400,268 C470,274 530,254 562,232 L562,262 C460,292 350,302 250,288 C150,274 60,282 0,296 Z"/>
      <path fill="url(#redBandA)" d="M0,218 C120,205 260,260 400,272 C470,278 530,258 562,238 L562,248 C500,272 440,280 380,278 C260,272 130,232 0,244 Z"/>
      <path fill="url(#redBandA)" d="M0,250 C130,240 260,280 380,286 C450,289 520,272 562,256 L562,260 C460,292 350,302 250,288 C150,274 60,282 0,296 Z"/>
      <path fill="url(#bowTone)" role="img" aria-label="Red gift ribbon bow tied across the corner" d="M467,0 L562,0 L562,86 C540,80 520,70 505,50 C490,32 475,16 467,0 Z"/>
    </svg>
    <div class="brand">
      <div class="brand__name">Maple Parcel</div>
      <div class="brand__tag">greeting card and gift wrap</div>
    </div>
    <div class="holder">Colin Madsey</div>
    <ul class="contacts">
      <li>Unit 37 / 18 Banksia ave West Torrin 2563
        <svg viewBox="0 0 20 18"><path stroke="none" d="M10,1 L19,9 L16.5,9 L16.5,17 L12,17 L12,12 L8,12 L8,17 L3.5,17 L3.5,9 L1,9 Z"/></svg></li>
      <li>0244879351
        <svg viewBox="0 0 20 18"><path stroke="none" d="M2,6 C2,2 18,2 18,6 L15,7 L14,5 C12,4 8,4 6,5 L5,7 Z M5,9 L15,9 L18,16 L2,16 Z"/></svg></li>
      <li>0244879352
        <svg viewBox="0 0 20 18"><path stroke="none" d="M5,1 L15,1 L15,7 L5,7 Z M1,8 L19,8 L19,17 L1,17 Z"/><path stroke="none" fill="#222" d="M4,11 L16,11 L16,12.5 L4,12.5 Z"/></svg></li>
      <li>maple.parcel@postvale.com
        <svg viewBox="0 0 20 18"><text x="10" y="15" text-anchor="middle" font-size="18" font-family="Ubuntu, sans-serif" stroke="none">@</text></svg></li>
    </ul>
  </section>

</div>
</body>
</html>
```